Accounting practice seeks business card redesign with existing logo

Accounting practice has logo and slogan but more needs modern professional business revision. Must be in a file format ready to print quality business cards.

Open to artistic ideas but for the brand recognition the features below must be incorporated:

- Logo: attached in EPS format (Logo now blue)
- Slogan: Proven Business Solutions... That Work! (in orange legible handwriting type font)
- Name: Daniel T Hoxley RBA AAT JP (letters in smaller font)
- Phone icon: 1800 531 908
- Mobile phone icon: 0412 385 714
- Web icon: www.kelnovagroup.com.au
- Email icon: admin@kelnovagroup.com.au
- See pics for dark blue/med blue line at bottom, this is a necessity.
- Globe that forms the 'dot' in the 'I' of KelNova is attached. It is too big at present.
- Rear side: pic attached. Note my logo is a watermark. I Will provide slightly revised wording details later. Please allow for a small white space at bottom of rear of card to write notes/appointment details.

I am open to ideas but must retain the above for brand recognition.

```html
<!DOCTYPE html>
<html lang="en">
<head>
<meta charset="utf-8">
<title>KelNova Solutions – Business Card</title>
<link rel="stylesheet" href="https://fonts.googleapis.com/css2?family=Lato:wght@300;400;700;900&display=swap">
<style>
  :root {
    --backdrop: #e9eaee;
    --navy-deep: #141f5a;
    --navy: #22317a;
    --navy-light: #34479a;
    --sky: #3b93d8;
    --sky-light: #5fb0ea;
    --white: #ffffff;
    --mist: rgba(255,255,255,0.72);
    --ghost: rgba(255,255,255,0.08);
  }
  * { box-sizing: border-box; margin: 0; padding: 0; }
  html, body { width: 1200px; height: 913px; overflow: hidden; }
  body {
    background: var(--backdrop);
    font-family: "Lato", Arial, sans-serif;
    color: var(--white);
    position: relative;
  }
  .card {
    position: absolute;
    top: 306px;
    width: 540px;
    height: 300px;
    border-radius: 18px;
    overflow: hidden;
    background: linear-gradient(160deg, var(--navy-light) 0%, var(--navy) 45%, var(--navy-deep) 100%);
    box-shadow: 0 10px 28px rgba(20,31,90,0.28);
  }
  .card--front { left: 40px; }
  .card--back { left: 620px; }

  /* front */
  .swirl-art {
    position: absolute; left: 150px; top: 20px; width: 260px; height: 260px;
    border-radius: 50%;
    background: radial-gradient(circle at 55% 55%, rgba(255,255,255,0.04) 0%, rgba(255,255,255,0.12) 45%, rgba(255,255,255,0.03) 70%, transparent 72%);
  }
  .logo {
    position: absolute; right: 30px; top: 26px;
    display: flex; align-items: center; gap: 8px;
    font-size: 30px; font-weight: 300; letter-spacing: 1px; color: var(--sky-light);
  }
  .logo__dot { width: 12px; height: 12px; border-radius: 50%; background: var(--sky-light); }
  .divider {
    position: absolute; left: 150px; right: 20px; top: 78px;
    height: 1px; background: var(--mist);
  }
  .online {
    position: absolute; right: 24px; top: 122px;
    font-size: 14px; line-height: 22px; list-style: none;
  }
  .online li, .phones li { display: flex; align-items: center; gap: 8px; }
  .icon { width: 13px; height: 13px; flex: none; }
  .holder { position: absolute; left: 30px; top: 178px; }
  .holder__name { font-size: 16px; font-weight: 900; }
  .holder__role { font-size: 10px; color: var(--mist); margin-top: 2px; padding-bottom: 4px; border-bottom: 1px solid var(--mist); width: 150px; }
  .phones { list-style: none; margin-top: 16px; font-size: 15px; line-height: 20px; }
  .band-front {
    position: absolute; left: 0; right: 0; bottom: 0; height: 34px;
  }

  /* back */
  .watermark {
    position: absolute; left: 150px; top: 92px;
    font-size: 92px; font-weight: 300; letter-spacing: 6px;
    color: var(--ghost);
  }
  .tagline {
    position: absolute; left: 26px; top: 22px; width: 330px;
    font-size: 15px; font-weight: 900; line-height: 17px;
  }
  .services {
    position: absolute; list-style: none;
    font-size: 17px; font-weight: 400; line-height: 19px;
  }
  .services--left { left: 26px; top: 150px; }
  .services--right { right: 26px; top: 30px; text-align: left; }
  .notes {
    position: absolute; left: 0; right: 0; bottom: 0; height: 36px;
    background: var(--white); color: var(--navy);
    font-size: 14px; padding: 9px 0 0 26px;
  }
</style>
</head>
<body>

<section class="card card--front" aria-label="Business card front">
  <div class="swirl-art" role="img" aria-label="Faint circular brand swirl decoration"></div>
  <div class="logo"><span>KelNova</span><span class="logo__dot"></span></div>
  <div class="divider"></div>
  <ul class="online">
    <li>
      <svg class="icon" viewBox="0 0 16 16"><circle cx="8" cy="8" r="7" fill="none" stroke="#fff" stroke-width="1.4"/><ellipse cx="8" cy="8" rx="3" ry="7" fill="none" stroke="#fff" stroke-width="1.2"/><line x1="1" y1="8" x2="15" y2="8" stroke="#fff" stroke-width="1.2"/></svg>
      www.kelnovagroup.com.au
    </li>
    <li>
      <svg class="icon" viewBox="0 0 16 16"><rect x="1" y="3" width="14" height="10" fill="#fff"/><path d="M1 3 L8 9 L15 3" fill="none" stroke="#22317a" stroke-width="1.4"/></svg>
      admin@kelnovagroup.com.au
    </li>
  </ul>
  <div class="holder">
    <p class="holder__name">Daniel T Hoxley</p>
    <p class="holder__role">Executive Chairman</p>
    <ul class="phones">
      <li>
        <svg class="icon" viewBox="0 0 16 16"><rect x="4" y="1" width="8" height="14" rx="1.5" fill="none" stroke="#fff" stroke-width="1.4"/><circle cx="8" cy="12.5" r="0.9" fill="#fff"/></svg>
        1800 531 908
      </li>
      <li>
        <svg class="icon" viewBox="0 0 16 16"><path d="M4 1.5 L6.5 4.5 L5 6.5 C6 8.5 7.5 10 9.5 11 L11.5 9.5 L14.5 12 L12.5 14.5 C7 14 2 9 1.5 3.5 Z" fill="#fff"/></svg>
        0412 385 714
      </li>
    </ul>
  </div>
  <svg class="band-front" viewBox="0 0 540 34" preserveAspectRatio="none">
    <polygon points="250,10 540,10 540,34 230,34" fill="#3b93d8"/>
    <polygon points="0,26 230,26 230,34 0,34" fill="#1c2a6e"/>
  </svg>
</section>

<section class="card card--back" aria-label="Business card back">
  <div class="watermark">KelNova</div>
  <p class="tagline">Your trusted provider fo quality business and accounting solutions, proven to work for small to medium business and tradies.</p>
  <ul class="services services--right">
    <li>Business Advice</li>
    <li>Tax Office Assistance</li>
    <li>Office Technology</li>
    <li>And Much More</li>
  </ul>
  <ul class="services services--left">
    <li>Bookkeeping</li>
    <li>Bas</li>
    <li>Cloud According</li>
    <li>Debt Recovery</li>
  </ul>
  <div class="notes">Next Appoinments:</div>
</section>

</body>
</html>
```